Product Sales Website Design - E-commerce - Shopify etc

We have been selling printing equipment for some time now and think that it will be useful to sell the products on the internet, using a simple e-commerce platform, such as shopify etc. There are roughly a few dozen products - so basically, the idea is to have a modern, simple and clean home page. When someone looks at it, they think, this is it - I want to buy here. I am not going to impose any ideas or say how I want it done.

Just so you know, at the moment there are three categories of products. One being printers, scanners and accessories.

I am excited by this whole project and don't want to have good designers backing out because they feel i am imposing restrictions. Feel free to impress me.

Industry/Entity Type

E-Commerce

Requirements
Must have
• integration with an e-commerce platform is a must or show how to integrate, so I can easily introduce further products.

```html
<!DOCTYPE html>
<html lang="en">
<head>
<meta charset="utf-8">
<title>Harlow Equipments — Home</title>
<link href="https://fonts.googleapis.com/css2?family=Carlito:wght@400;700&family=Arimo:wght@400&display=swap" rel="stylesheet">
<style>
:root{
  --ink:#1a1a1a;
  --muted:#555;
  --green:#45a019;
  --green-light:#6cbf3a;
  --red-accent:#e0401e;
  --hero:#000;
  --rule:#d6d6d6;
  --band:#d9d9d9;
  --footer:#6b6b6b;
  --footer-text:#f0f0f0;
  --box-border:#cfcfcf;
}
*{box-sizing:border-box;margin:0;padding:0}
html,body{width:1200px;height:2278px;overflow:hidden;background:#fff}
body{position:relative;font-family:"Carlito",Calibri,sans-serif;color:var(--ink)}
.abs{position:absolute}

/* top bar */
.lang{left:61px;top:11px;width:118px;height:24px;border-radius:12px;background:#e6e6e6;font-size:13px;color:#444;display:flex;align-items:center;padding-left:12px;gap:8px}
.lang .flag{width:16px;height:10px;background:#3a4f8c;border:1px solid #c33}
.lang .caret{margin-left:auto;margin-right:12px;width:0;height:0;border-left:4px solid transparent;border-right:4px solid transparent;border-top:5px solid #666}
.account{left:196px;top:13px;font-size:14px;color:#444;letter-spacing:.3px}
.search{left:867px;top:11px;width:278px;height:39px;border:1px solid #d5d5d5;border-radius:8px;background:#fafafa;box-shadow:inset 0 1px 2px rgba(0,0,0,.08);font-size:13px;font-style:italic;color:#aaa;padding:11px 12px}
.search svg{position:absolute;right:10px;top:9px}
.brand{left:0;width:1200px;top:66px;text-align:center;font-family:"Arimo",Arial,sans-serif;font-size:29px;letter-spacing:.5px;color:#111}
.top-rule{left:61px;top:130px;width:1078px;height:1px;background:var(--rule)}
.nav{top:147px;left:0;width:1200px;font-size:15px;color:#222}
.nav a{position:absolute;color:inherit;text-decoration:none;white-space:nowrap}
.nav a.active{color:#666}
.nav .indicator{position:absolute;left:316px;top:-17px;width:50px;height:3px;background:#bbb}
.cart{left:993px;top:146px;font-size:15px;color:#444;display:flex;align-items:center;gap:8px}
.cart b{font-weight:400;color:var(--red-accent)}

/* hero */
.hero{left:0;top:190px;width:1200px;height:454px;background:var(--hero)}
.hero h1{position:absolute;left:106px;top:136px;font-size:25px;font-weight:400;color:#fff;letter-spacing:.3px}
.hero p{position:absolute;left:106px;top:176px;width:335px;font-size:13.5px;line-height:25.5px;color:#ccc}
.btn{display:flex;align-items:center;justify-content:center;background:var(--green);color:#fff;font-size:17px;text-decoration:none}
.hero .btn{position:absolute;left:324px;top:304px;width:115px;height:48px;border-radius:2px}
.hero .visual{position:absolute;left:483px;top:45px;width:596px;height:357px;border-radius:6px;background:radial-gradient(ellipse at 50% 55%,#6e6e6e 0%,#3b3b3b 45%,#000 75%)}
.arrow{position:absolute;top:176px;width:54px;height:64px;border:1px solid #444;border-radius:4px;background:#0c0c0c;display:flex;align-items:center;justify-content:center}
.arrow.prev{left:11px}.arrow.next{left:1132px}

/* section titles */
.section-title{left:0;width:1200px;text-align:center;font-size:34px;font-weight:400;letter-spacing:.5px}

/* products */
.product{width:221px;text-align:center}
.product .name{font-size:17px;color:#333;height:20px}
.product .frame{margin-top:20px;height:216px;border:1px solid var(--box-border);box-shadow:0 0 3px rgba(0,0,0,.08);position:relative;display:flex;align-items:center;justify-content:center}
.product .photo{width:160px;height:140px;border-radius:6px;background:radial-gradient(ellipse,#8a8a8a 0%,#cfcfcf 55%,#fff 80%)}
.product .price{margin-top:10px;font-size:18px}
.product .price s{color:#444}
.product .price span{color:var(--green)}
.quick{position:absolute;left:0;right:0;top:75px}
.quick div{height:37px;display:flex;align-items:center;justify-content:center;color:#fff;font-size:15px;font-weight:700}
.quick .dark{background:#111}
.quick .light{background:var(--green-light)}
.view-all{left:447px;top:1432px;width:262px;height:48px;border-radius:2px}
.mid-rule{left:102px;top:1502px;width:993px;height:1px;background:#bbb}

/* news */
.news{width:219px}
.news .photo{height:100px;background:linear-gradient(135deg,#d8d8d8,#555 60%,#222)}
.news h3{margin-top:14px;font-size:13.5px;font-weight:400;color:#111}
.news p{margin-top:3px;font-size:12px;line-height:25.5px;color:#555}

/* newsletter */
.newsletter{left:0;top:1970px;width:1200px;height:167px;background:var(--band)}
.newsletter h2{position:absolute;top:26px;width:100%;text-align:center;font-size:34px;font-weight:400;letter-spacing:.5px}
.newsletter .lead{position:absolute;left:188px;top:96px;font-size:16px;color:#222}
.newsletter .field{position:absolute;left:688px;top:90px;width:272px;height:36px;background:#fff;font-size:12px;font-style:italic;color:#999;padding:10px 14px}
.newsletter .subscribe{position:absolute;left:972px;top:90px;width:134px;height:36px;background:#555;color:#fff;font-size:17px;display:flex;align-items:center;justify-content:center}

/* footer */
.footer{left:0;top:2137px;width:1200px;height:141px;background:var(--footer);color:var(--footer-text)}
.footer .links{position:absolute;left:111px;top:40px;font-size:13px;word-spacing:2px}
.footer .copy{position:absolute;left:111px;top:91px;font-size:13px;color:#ddd}
.social{position:absolute;top:42px;width:28px;height:28px;background:#5a84c4;border-radius:2px}
</style>
</head>
<body>

<header>
  <div class="abs lang"><span class="flag"></span>English<span class="caret"></span></div>
  <div class="abs account">LOG IN &nbsp;|&nbsp; REGISTER</div>
  <div class="abs search">Search your products
    <svg width="22" height="22" viewBox="0 0 22 22"><circle cx="9" cy="9" r="6.5" fill="none" stroke="#222" stroke-width="3"/><line x1="14" y1="14" x2="20" y2="20" stroke="#222" stroke-width="3.5" stroke-linecap="round"/></svg>
  </div>
  <div class="abs brand">HARLOW EQUIPMENTS</div>
  <div class="abs top-rule"></div>
  <nav class="abs nav">
    <span class="indicator"></span>
    <a class="active" style="left:320px">HOME</a>
    <a style="left:424px">ABOUT US</a>
    <a style="left:548px">PRODUCTS</a>
    <a style="left:676px">SERVICES</a>
    <a style="left:796px">CONTACT US</a>
  </nav>
  <div class="abs cart">
    <svg width="26" height="24" viewBox="0 0 26 24"><path d="M1 3h4l3 12h13l3-9H7" fill="none" stroke="#666" stroke-width="2"/><circle cx="10" cy="20" r="2" fill="#666"/><circle cx="19" cy="20" r="2" fill="#666"/></svg>
    CART: &nbsp;<b>(0) ITEMS</b>
  </div>
</header>

<section class="abs hero">
  <div class="arrow prev"><svg width="14" height="34"><polyline points="12,2 3,17 12,32" fill="none" stroke="#aaa" stroke-width="1.5"/></svg></div>
  <h1>LOREM IPSUM DOLOR SIT AMET</h1>
  <p>Consectetur adipisicing elit, sed do eiusmod tempor incididunt ut labore et dolore magna aliqua. Consectetur adipisicing elit, sed do eiusmod tempor incididunt ut labore et dolore magna aliqua.</p>
  <a class="btn">SHOP NOW</a>
  <div class="visual" role="img" aria-label="Product photo of an all-in-one office printer beside a compact printer feeding paper"></div>
  <div class="arrow next"><svg width="14" height="34"><polyline points="2,2 11,17 2,32" fill="none" stroke="#aaa" stroke-width="1.5"/></svg></div>
</section>

<h2 class="abs section-title" style="top:713px">LATEST PRODUCTS</h2>

<div class="abs product" style="left:106px;top:798px">
  <div class="name">Corvel Printers</div>
  <div class="frame"><div class="photo" role="img" aria-label="Laser printer product photo"></div>
    <div class="quick"><div class="dark">QUICK SHOP</div><div class="light">ADD TO CART</div></div></div>
  <div class="price"><s>$200</s> <span>$175</span></div>
</div>
<div class="abs product" style="left:355px;top:798px">
  <div class="name">Corvel Printers</div>
  <div class="frame"><div class="photo" role="img" aria-label="Large format plotter product photo"></div></div>
  <div class="price"><s>$200</s> <span>$175</span></div>
</div>
<div class="abs product" style="left:608px;top:798px">
  <div class="name">Corvel Printers</div>
  <div class="frame"><div class="photo" role="img" aria-label="Inkjet photo printer product photo"></div></div>
  <div class="price"><s>$200</s> <span>$175</span></div>
</div>
<div class="abs product" style="left:864px;top:798px">
  <div class="name">Corvel Printers</div>
  <div class="frame"><div class="photo" role="img" aria-label="All-in-one printer scanner product photo"></div></div>
  <div class="price"><s>$200</s> <span>$175</span></div>
</div>

<div class="abs product" style="left:106px;top:1128px">
  <div class="name">Corvel Printers</div>
  <div class="frame"><div class="photo" role="img" aria-label="Laser printer product photo"></div></div>
  <div class="price"><s>$200</s> <span>$175</span></div>
</div>
<div class="abs product" style="left:355px;top:1128px">
  <div class="name">Corvel Printers</div>
  <div class="frame"><div class="photo" role="img" aria-label="Large format plotter product photo"></div></div>
  <div class="price"><s>$200</s> <span>$175</span></div>
</div>
<div class="abs product" style="left:608px;top:1128px">
  <div class="name">Corvel Printers</div>
  <div class="frame"><div class="photo" role="img" aria-label="Inkjet photo printer product photo"></div></div>
  <div class="price"><s>$200</s> <span>$175</span></div>
</div>
<div class="abs product" style="left:864px;top:1128px">
  <div class="name">Corvel Printers</div>
  <div class="frame"><div class="photo" role="img" aria-label="All-in-one printer scanner product photo"></div></div>
  <div class="price"><s>$200</s> <span>$175</span></div>
</div>

<a class="abs btn view-all">VIEW ALL LATEST PRODUCTS</a>
<div class="abs mid-rule"></div>

<h2 class="abs section-title" style="top:1556px">LATEST NEWS</h2>

<article class="abs news" style="left:111px;top:1630px">
  <div class="photo" role="img" aria-label="Close-up of a printer outputting a page"></div>
  <h3>Lorem ipsum dolor sit amet</h3>
  <p>consectetur adipisicing elit, sed do eiusmod tempor incididunt ut labore et dolore magna aliqua. Excepteur sint occaecat cupidatat non proident, sunt in culpa qui officia deserunt mollit anim id est laborum.</p>
</article>
<article class="abs news" style="left:365px;top:1630px">
  <div class="photo" role="img" aria-label="Wide format printer in an office"></div>
  <h3>Lorem ipsum dolor sit amet</h3>
  <p>consectetur adipisicing elit, sed do eiusmod tempor incididunt ut labore et dolore magna aliqua. Excepteur sint occaecat cupidatat non proident, sunt in culpa qui officia deserunt mollit anim id est laborum.</p>
</article>
<article class="abs news" style="left:615px;top:1630px">
  <div class="photo" role="img" aria-label="Office copier machines in a print room" style="background:linear-gradient(135deg,#e8e0c8,#a89a78 60%,#6c624a)"></div>
  <h3>Lorem ipsum dolor sit amet</h3>
  <p>consectetur adipisicing elit, sed do eiusmod tempor incididunt ut labore et dolore magna aliqua. Excepteur sint occaecat cupidatat non proident, sunt in culpa qui officia deserunt mollit anim id est laborum.</p>
</article>
<article class="abs news" style="left:866px;top:1630px">
  <div class="photo" role="img" aria-label="Printer output tray with a colour print" style="background:linear-gradient(160deg,#222,#3a4a7a 55%,#c0c8e0)"></div>
  <h3>Lorem ipsum dolor sit amet</h3>
  <p>consectetur adipisicing elit, sed do eiusmod tempor incididunt ut labore et dolore magna aliqua. Excepteur sint occaecat cupidatat non proident, sunt in culpa qui officia deserunt mollit anim id est laborum.</p>
</article>

<section class="abs newsletter">
  <h2>NEWSLETTER SIGNUP</h2>
  <div class="lead">Enter your Email Id to signup and get our daily updates to your Email</div>
  <div class="field">Your Email Id</div>
  <div class="subscribe">SUBSCRIBE</div>
</section>

<footer class="abs footer">
  <div class="links">Home &nbsp;|&nbsp; About &nbsp;|&nbsp; Products &nbsp;|&nbsp; Services &nbsp;|&nbsp; Register &nbsp;|&nbsp; Login &nbsp;|&nbsp; Privacy &nbsp;|&nbsp; Terms of Use &nbsp;|&nbsp; Legal Policy</div>
  <div class="copy">All Rights reserved. Copyrights @ 2013 Harlow Equipments.</div>
  <span class="social" style="left:1003px" aria-label="Social link"></span>
  <span class="social" style="left:1043px;background:#4aa8dc" aria-label="Social link"></span>
  <span class="social" style="left:1089px;background:#3d7eb4" aria-label="Social link"></span>
</footer>

</body>
</html>
```